Redmoor Asphalt Paving needs awesome postcard design

Business to business post card design needed. We are an asphalt paving contractor looking to attract commercial and industrial customers who need pavement replacement and repairs. We do: Asphalt paving, milling, crack filling and striping.

Postcard should have the following words:
Redmoor Asphalt Paving
www.redmoorpavingco.example
Asphalt Paving
Milling
Hot Rubber Crack Filling
Striping

Michigan's Premier Paving Contractor
(555) 728-1956

Address for return area on card:
Redmoor Asphalt Paving
48213 Thornvale
Larkfield, MI 40917

Target Market(s)

Building owners and property managers

Industry/Entity Type

Ashpalt Paving

Font styles to use
Sans Serif

Requirements
Must have
• Logo, phone number (555) 728-1956, tagline: "Michigan's Premier Paving Contractor" website address and: Paving, milling, hot rubber crack filling, seal coating
Nice to have
• Picture of a newly paved parking lot with or without stripes
Should not have
• Homeowner driveway - WE DO NOT WANT TO ATTRACT RESIDENTIAL WORK

```html
<!DOCTYPE html>
<html lang="en">
<head>
<meta charset="utf-8">
<title>Redmoor Asphalt Paving – Postcard</title>
<link href="https://fonts.googleapis.com/css2?family=Roboto+Condensed:wght@300;400;700&display=swap" rel="stylesheet">
<style>
  :root {
    --backdrop: #7b7b7b;
    --paper: #ffffff;
    --ink: #000000;
    --ink-soft: #1a1a1a;
    --reverse: #ffffff;
    --reverse-soft: #d4d4d4;
    --font: "Roboto Condensed", "Arial Narrow", sans-serif;
  }
  * { box-sizing: border-box; margin: 0; padding: 0; }
  html, body {
    width: 1199px; height: 1200px; overflow: hidden;
    background: var(--backdrop);
    font-family: var(--font);
    color: var(--ink);
  }
  .stage {
    position: absolute; left: 0; top: 0;
    width: 960px; height: 961px;
    transform: scale(1.249);
    transform-origin: 0 0;
  }
  .postcard {
    position: absolute; left: 156px;
    width: 648px; height: 431px;
    background: var(--paper);
    overflow: hidden;
    box-shadow: 0 2px 6px rgba(0,0,0,.35);
  }
  .postcard--front { top: 35px; }
  .postcard--back { top: 494px; }
  .postcard__shapes { position: absolute; inset: 0; width: 648px; height: 431px; }
  .postcard__shapes .fill { fill: var(--ink); }
  .postcard__shapes .stripe { fill: none; stroke: var(--paper); stroke-width: 8; }
  .postcard__shapes .panel { fill: var(--paper); }

  .brand-block {
    position: absolute; left: 34px; top: 50px; width: 183px;
    text-align: center; line-height: 1;
  }
  .brand-block__name { font-weight: 700; font-size: 17px; white-space: nowrap; }
  .brand-block__tagline { font-weight: 700; font-size: 6.4px; margin-top: 4px; letter-spacing: .1px; }
  .brand-block__phone { font-weight: 700; font-size: 9px; margin-top: 8px; letter-spacing: .6px; }
  .brand-block__web { font-weight: 700; font-size: 9.5px; margin-top: 2px; }

  .text { position: absolute; line-height: 1; white-space: nowrap; }
  .align-right { right: 40px; text-align: right; }

  .headline { font-weight: 700; font-size: 23px; top: 86px; letter-spacing: .2px; }
  .site { font-weight: 400; font-size: 15px; top: 119px; }
  .slogan { font-weight: 400; font-size: 21px; line-height: 28px; top: 183px; }
  .phone { font-weight: 400; font-size: 16px; top: 241px; }

  .services { position: absolute; left: 32px; top: 314px; list-style: none; }
  .services li { font-size: 16px; line-height: 22px; display: flex; align-items: center; }
  .services svg { width: 11px; height: 11px; margin-right: 14px; fill: var(--ink); }

  .return-label { font-weight: 700; font-size: 15px; top: 321px; color: var(--reverse); }
  .return-address {
    font-weight: 300; font-size: 15px; line-height: 21px; top: 341px;
    color: var(--reverse-soft); white-space: normal;
  }

  .stamp-box {
    position: absolute; left: 517px; top: 31px; width: 88px; height: 91px;
    border: 1.5px solid var(--ink);
  }
  .address-line {
    position: absolute; left: 366px; width: 239px; height: 0;
    border-top: 1.5px solid var(--ink-soft);
  }
  .address-line--one { top: 334px; }
  .address-line--two { top: 372px; }

  .back-headline { left: 32px; top: 335px; font-weight: 700; font-size: 20px; letter-spacing: .2px; color: var(--reverse); }
  .back-site { left: 32px; top: 364px; font-weight: 400; font-size: 15px; color: var(--reverse); }
</style>
</head>
<body>
<div class="stage">

  <section class="postcard postcard--front">
    <svg class="postcard__shapes" viewBox="0 0 648 431" aria-hidden="true">
      <polygon class="fill" points="325,0 377,0 232,214 188,208"/>
      <polygon class="fill" points="0,173 648,310 648,431 0,431"/>
      <polyline class="stripe" points="0,227 341,297 332,431"/>
      <polygon class="panel" points="0,239 322,305 303,431 0,431"/>
    </svg>

    <div class="brand-block">
      <div class="brand-block__name">Redmoor Asphalt Paving</div>
      <div class="brand-block__tagline">MICHIGAN'S PREMIER PAVING CONTRACTOR</div>
      <div class="brand-block__phone">555.728.1956</div>
      <div class="brand-block__web">WWW.REDMOORPAVINGCO.EXAMPLE</div>
    </div>

    <h1 class="text align-right headline">REDMOOR ASPHALT PAVING</h1>
    <p class="text align-right site">www.redmoorpavingco.example</p>
    <p class="text align-right slogan">Michigan's Premier<br>Paving Contractor</p>
    <p class="text align-right phone">(555) 728-1956</p>

    <ul class="services">
      <li><svg viewBox="0 0 10 10"><path d="M5 0l1.2 3 3-1.2-1.7 2.7L10 6.1 6.9 6.5 7 10 5 7.4 3 10l.1-3.5L0 6.1l2.5-1.6L.8 1.8l3 1.2z"/></svg>Asphalt Paving</li>
      <li><svg viewBox="0 0 10 10"><path d="M5 0l1.2 3 3-1.2-1.7 2.7L10 6.1 6.9 6.5 7 10 5 7.4 3 10l.1-3.5L0 6.1l2.5-1.6L.8 1.8l3 1.2z"/></svg>Milling</li>
      <li><svg viewBox="0 0 10 10"><path d="M5 0l1.2 3 3-1.2-1.7 2.7L10 6.1 6.9 6.5 7 10 5 7.4 3 10l.1-3.5L0 6.1l2.5-1.6L.8 1.8l3 1.2z"/></svg>Hot Rubber Crack Filling</li>
      <li><svg viewBox="0 0 10 10"><path d="M5 0l1.2 3 3-1.2-1.7 2.7L10 6.1 6.9 6.5 7 10 5 7.4 3 10l.1-3.5L0 6.1l2.5-1.6L.8 1.8l3 1.2z"/></svg>Striping</li>
    </ul>

    <p class="text align-right return-label">Address for return area on card:</p>
    <p class="text align-right return-address">Redmoor Asphalt Paving<br>48213 Thornvale<br>Larkfield, MI 40917</p>
  </section>

  <section class="postcard postcard--back">
    <svg class="postcard__shapes" viewBox="0 0 648 431" aria-hidden="true">
      <polygon class="fill" points="362,0 389,0 213,186 309,224 298,285 0,174 0,160 155,216"/>
      <polygon class="fill" points="0,186 297,297 297,431 0,431"/>
    </svg>

    <div class="brand-block">
      <div class="brand-block__name">Redmoor Asphalt Paving</div>
      <div class="brand-block__tagline">MICHIGAN'S PREMIER PAVING CONTRACTOR</div>
      <div class="brand-block__phone">555.728.1956</div>
      <div class="brand-block__web">WWW.REDMOORPAVINGCO.EXAMPLE</div>
    </div>

    <div class="stamp-box"></div>
    <div class="address-line address-line--one"></div>
    <div class="address-line address-line--two"></div>

    <h2 class="text back-headline">REDMOOR ASPHALT PAVING</h2>
    <p class="text back-site">www.redmoorpavingco.example</p>
  </section>

</div>
</body>
</html>
```